Brochure & Business card design

Looking for a new business card design i want it to be modern and sharp looking i usually order plastic business cards, and i would like to make the colors like the logo teal/charcoal i will like to have our services on icons with words.... our services are
ROOFING GUTTERS PAINTING PRESSURE WASHING EXTERIOR DESIGN & ATTIC VENTILATION. I also want to add my credentials

Target Market(s)

Oregon local market

Industry/Entity Type

Residential Construction

Contact Information for Business Card

Business info, services, number, website

Font styles to use
Serif
Sans Serif

Colors
33b8a4
5c5c5c
ffffff

Requirements
Must have
• Dale Finch
• Cell:
• Office:
• Email:
• Website:
• also i need our social media icons
• Services ROOFING GUTTERS PAINTING PRESSURE WASHING EXTERIOR DESIGN & ATTIC VENTILATION
• -icons for number, web, email, cell
• OR #584312
• Wa #KTRABLD461X7
Nice to have
• -Clean design Front & Back
• -Icons
• -shape House just like logo design
• -First Impression
Should not have
• Not Busy or lost of eye contact

```html
<!DOCTYPE html>
<html lang="en">
<head>
<meta charset="utf-8">
<title>Ridgeline Home Exteriors – Business Card</title>
<link href="https://fonts.googleapis.com/css2?family=Montserrat:wght@600;700&family=Mulish:wght@400;600;700;800&display=swap" rel="stylesheet">
<style>
  :root {
    --teal: #33b8a4;
    --charcoal: #5c5c5c;
    --charcoal-dark: #454547;
    --white: #ffffff;
    --backdrop: #5a6068;
    --ink: #4a4a4a;
    --badge-red: #d8312b;
    --badge-black: #1d1d1d;
  }
  * { margin: 0; padding: 0; box-sizing: border-box; }
  html, body { width: 1200px; height: 903px; overflow: hidden; }
  body {
    background: var(--backdrop);
    font-family: "Mulish", Arial, sans-serif;
    color: var(--ink);
    position: relative;
  }
  .card {
    position: absolute;
    left: 250px;
    width: 700px;
    height: 400px;
    overflow: hidden;
    box-shadow: 0 10px 30px rgba(0,0,0,.35);
  }
  /* ---------- Front ---------- */
  .card-front { top: 32px; background: var(--white); }
  .brand {
    position: absolute; left: 70px; top: 42px; width: 240px;
    text-align: center;
  }
  .brand-mark {
    display: inline-block; width: 26px; height: 26px;
    background: var(--charcoal); margin-bottom: 8px;
  }
  .brand-name {
    font-weight: 800; color: var(--teal); font-size: 24px; line-height: 1.1;
  }
  .brand-tagline {
    font-size: 10px; letter-spacing: 1.5px; text-transform: uppercase;
    color: var(--charcoal); margin-top: 6px; font-weight: 700;
  }
  .services-title {
    position: absolute; left: 70px; top: 188px; width: 240px; text-align: center;
    font-weight: 800; color: var(--teal); font-size: 19px; letter-spacing: 1px;
  }
  .services {
    position: absolute; left: 36px; top: 222px;
    display: grid; grid-template-columns: 110px 180px; row-gap: 14px;
    list-style: none;
  }
  .service {
    display: flex; align-items: center; gap: 9px;
    font-size: 16.5px; font-weight: 600; color: var(--ink); white-space: nowrap;
  }
  .service svg { width: 22px; height: 22px; flex: none; }
  .divider {
    position: absolute; left: 352px; top: 48px; width: 2px; height: 268px;
    background: var(--charcoal); opacity: .75;
  }
  .contact { position: absolute; left: 378px; top: 50px; width: 300px; }
  .person-name {
    font-family: "Montserrat", Arial, sans-serif; font-weight: 700;
    color: var(--teal); font-size: 33px; letter-spacing: 1.5px; margin-left: 4px;
  }
  .contact-list { list-style: none; margin-top: 16px; }
  .contact-item {
    display: flex; align-items: flex-start; gap: 12px;
    font-size: 16px; line-height: 1.25; color: var(--ink); margin-bottom: 16px;
  }
  .contact-item svg { width: 24px; height: 24px; flex: none; }
  .licenses {
    position: absolute; left: 372px; top: 318px; font-size: 14px; color: var(--ink);
  }
  .licenses .sep { margin: 0 10px; font-weight: 700; }
  .badge { position: absolute; top: 352px; height: 28px; border-radius: 3px; }
  .badge-cert { left: 400px; width: 80px; background: var(--badge-red); }
  .badge-accredited { left: 525px; width: 72px; background: var(--badge-black); }
  .social-band {
    position: absolute; left: 0; bottom: 0; width: 700px; height: 52px;
  }
  .social-handle {
    position: absolute; left: 30px; bottom: 14px;
    color: var(--white); font-size: 16px; font-weight: 700; letter-spacing: .5px;
  }
  /* ---------- Back ---------- */
  .card-back { top: 470px; background: var(--teal); }
  .back-brand {
    position: absolute; left: 0; right: 0; top: 105px; text-align: center; color: var(--white);
  }
  .back-brand .brand-mark { background: var(--white); width: 34px; height: 34px; margin-bottom: 12px; }
  .back-brand .brand-name { color: var(--white); font-size: 36px; }
  .back-brand .brand-tagline { color: var(--white); font-size: 13px; margin-top: 10px; }
  .back-band { position: absolute; left: 0; bottom: 0; width: 700px; height: 90px; }
  .back-web {
    position: absolute; left: 0; right: 0; bottom: 18px; text-align: center;
    color: var(--white); font-size: 19px; font-weight: 700; letter-spacing: 2px;
  }
</style>
</head>
<body>

<section class="card card-front" aria-label="Business card front">
  <div class="brand">
    <span class="brand-mark"></span>
    <div class="brand-name">Ridgeline<br>Home Exteriors</div>
    <div class="brand-tagline">When quality matters</div>
  </div>

  <h2 class="services-title">SERVICES</h2>
  <ul class="services">
    <li class="service">
      <svg viewBox="0 0 24 24" fill="none" stroke="#33b8a4" stroke-width="1.6"><path d="M3 18 L6 6 H18 L21 18 Z"/><path d="M4.5 12 H19.5 M9 6 L8 18 M15 6 L16 18 M12 6 V18"/></svg>
      Roofing
    </li>
    <li class="service">
      <svg viewBox="0 0 24 24" fill="none" stroke="#33b8a4" stroke-width="1.6"><circle cx="7" cy="12" r="3"/><path d="M10 12 H15 M17 9 L21 6 M17 12 H22 M17 15 L21 18"/><path d="M7 15 V21"/></svg>
      Pressure Washing
    </li>
    <li class="service">
      <svg viewBox="0 0 24 24" fill="none" stroke="#33b8a4" stroke-width="1.6"><rect x="4" y="4" width="6" height="6" rx="1"/><rect x="14" y="4" width="6" height="6" rx="1"/><rect x="4" y="14" width="6" height="6" rx="1"/><rect x="14" y="14" width="6" height="6" rx="1"/></svg>
      Gutters
    </li>
    <li class="service">
      <svg viewBox="0 0 24 24" fill="none" stroke="#33b8a4" stroke-width="1.6"><rect x="4" y="3" width="16" height="18"/><path d="M4 3 L20 21 M12 3 V21 M4 12 H20"/></svg>
      Exterior Design
    </li>
    <li class="service">
      <svg viewBox="0 0 24 24" fill="none" stroke="#33b8a4" stroke-width="1.6"><rect x="12" y="3" width="8" height="8" rx="1" transform="rotate(45 16 7)"/><path d="M12 11 L5 18"/><path d="M3 21 L6 17 L8 19 Z" fill="#33b8a4"/></svg>
      Painting
    </li>
    <li class="service">
      <svg viewBox="0 0 24 24" fill="none" stroke="#33b8a4" stroke-width="1.6"><circle cx="12" cy="12" r="9"/><path d="M12 3 V21 M3 12 H21 M5.6 5.6 L18.4 18.4 M18.4 5.6 L5.6 18.4"/></svg>
      Attic Ventilation
    </li>
  </ul>

  <div class="divider"></div>

  <div class="contact">
    <h1 class="person-name">DALE FINCH</h1>
    <ul class="contact-list">
      <li class="contact-item">
        <svg viewBox="0 0 24 24"><circle cx="12" cy="12" r="11" fill="#33b8a4"/><path d="M12 5 a4.5 4.5 0 0 1 4.5 4.5 c0 3.2-4.5 8.5-4.5 8.5 s-4.5-5.3-4.5-8.5 A4.5 4.5 0 0 1 12 5z" fill="#fff"/><circle cx="12" cy="9.5" r="1.8" fill="#33b8a4"/></svg>
        <span>Cedar Falls, OR 97999,<br>United States</span>
      </li>
      <li class="contact-item">
        <svg viewBox="0 0 24 24"><circle cx="12" cy="12" r="11" fill="#33b8a4"/><path d="M8 6 L10.5 8.5 L9.2 10.3 C10 12 11.8 13.8 13.7 14.8 L15.5 13.5 L18 16 L16.3 18 C11.5 17.5 6.5 12.5 6 7.7 Z" fill="#fff"/></svg>
        <span>(541) 555-0148</span>
      </li>
      <li class="contact-item">
        <svg viewBox="0 0 24 24"><circle cx="12" cy="12" r="11" fill="#33b8a4"/><rect x="6" y="8" width="12" height="8.5" rx="1" fill="#fff"/><path d="M6.5 8.5 L12 13 L17.5 8.5" fill="none" stroke="#33b8a4" stroke-width="1.3"/></svg>
        <span>info@ridgelinehomeext.com</span>
      </li>
      <li class="contact-item">
        <svg viewBox="0 0 24 24"><circle cx="12" cy="12" r="11" fill="#33b8a4"/><g fill="none" stroke="#fff" stroke-width="1.3"><circle cx="12" cy="12" r="6.5"/><ellipse cx="12" cy="12" rx="3" ry="6.5"/><path d="M5.5 12 H18.5 M6.5 9 H17.5 M6.5 15 H17.5"/></g></svg>
        <span>www.ridgelinehomeext.com</span>
      </li>
    </ul>
  </div>

  <p class="licenses">OR #584312<span class="sep">|</span>Wa #KTRABLD461X7</p>
  <div class="badge badge-cert" role="img" aria-label="Roofing certification badge"></div>
  <div class="badge badge-accredited" role="img" aria-label="Accredited business badge"></div>

  <svg class="social-band" viewBox="0 0 700 52" preserveAspectRatio="none">
    <polygon points="0,0 300,0 335,52 0,52" fill="var(--charcoal-dark)"/>
    <rect x="335" y="44" width="365" height="8" fill="var(--teal)"/>
  </svg>
  <span class="social-handle">@ridgelinehomeext</span>
</section>

<section class="card card-back" aria-label="Business card back">
  <div class="back-brand">
    <span class="brand-mark"></span>
    <div class="brand-name">Ridgeline Home Exteriors</div>
    <div class="brand-tagline">When quality matters</div>
  </div>
  <svg class="back-band" viewBox="0 0 700 90" preserveAspectRatio="none">
    <polygon points="0,30 160,30 180,10 520,10 540,30 700,30 700,90 0,90" fill="var(--white)"/>
    <polygon points="0,38 165,38 185,18 515,18 535,38 700,38 700,90 0,90" fill="var(--charcoal-dark)"/>
  </svg>
  <span class="back-web">WWW.RIDGELINEHOMEEXT.COM</span>
</section>

</body>
</html>
```